Illustrationen für Datenbankhierarchie
Schnelle Umsetzung von Wünschen und sehr gute Kommunikation und Arbeit! Gerne wieder!
Zielgruppe
Unser Produkt ist eine cloudbasierte Auftragsverwaltung und Warenwirtschaft für Veranstaltungsdienstleister.
Weitere Infos und eine Demo gibt es auf www.klangwerk-portal.de
Aufgabenstellung
Wir suchen eine Illustration, die unseren Kunden die Hierarchie in unserer Datenbank anschaulich erklärt. Wir legen Wert darauf, dass wir eine offene AI Datei bekommen, um später ggf. das Format oder die Texte ändern zu können.
Die bestehende Hierarchie bekommen Sie anhand unserer aktuellen Illustration.
Wir verwenden folgende Strukturebenen:
Artikel: Das Equipment gibt die Attribute der dazugehörigen Equipments an. Artikel sind nicht real am Lager vorhanden sondern vom Prinzip die Typvorgaben der Equipments. (Beispiel: Name:Scheinwerfer; Bild: 123.jpg; Gewicht:0,5kg; Artikelgruppe: Bühnenscheinwerfer; usw.)
Equipment: Equipments sind die real vorhandenen Gegenstände am Lager und im Bestand des Kunden. Zu einem Artikel kann es beliebig viele Equipments geben. (Beispiel: Scheinwerfer Nr. 1-24)
Equipmentset: Ist eine Sammlung aus Equipments, die miteinander verbunden sein können und immer zusammen genutzt werden. (Beispiel: Scheinwerferbar mit 6 Scheinwerfern)
Case: Behälter für Equipments, die fest zugeordnet sind.
Anlage: Sammlung von Equipments und/oder Equipmentsets und/oder Cases als Projekt.

```html
<!DOCTYPE html>
<html lang="de">
<head>
<meta charset="utf-8">
<title>klangwerk-portal.de – Datenbankhierarchie</title>
<link rel="stylesheet" href="https://fonts.googleapis.com/css2?family=Arimo:wght@400;700&display=swap">
<style>
  :root {
    --brand-blue: #4a9cc8;
    --tile-top: #55b3e3;
    --tile-bottom: #2b9dd3;
    --tile-edge: #8794a3;
    --ring-teal: #0aa9a0;
    --ring-blue: #1466be;
    --text-dark: #1d1d1b;
    --text-grey: #505a64;
    --bracket: #6e6e6e;
    --footer-bg: #404040;
    --white: #ffffff;
  }
  * { box-sizing: border-box; margin: 0; padding: 0; }
  html, body { width: 849px; height: 1200px; overflow: hidden; background: var(--white); }
  body { font-family: "Arimo", Helvetica, Arial, sans-serif; color: var(--text-dark); }
  .poster { position: relative; width: 849px; height: 1200px; overflow: hidden; }

  .header { position: absolute; left: 0; top: 0; width: 849px; height: 107px; background: var(--white); }
  .brand-mark { position: absolute; left: 43px; top: 24px; width: 64px; height: 64px; border-radius: 12px; background: var(--brand-blue); }
  .brand-name { position: absolute; left: 123px; top: 22px; font-size: 36px; font-weight: 400; color: var(--brand-blue); letter-spacing: -0.5px; }
  .brand-tagline { position: absolute; left: 124px; top: 65px; font-size: 15px; color: var(--text-grey); }

  .rule { position: absolute; left: 0; width: 849px; height: 2px; background: linear-gradient(90deg, var(--ring-blue), var(--ring-teal)); }

  .backdrop {
    position: absolute; left: 0; top: 109px; width: 849px; height: 1039px;
    background:
      radial-gradient(ellipse 320px 260px at 640px 200px, rgba(120,120,125,0.55), transparent 70%),
      linear-gradient(160deg, #b9b9bd 0%, #d6d8e2 22%, #e4e6ef 45%, #dfe2ec 70%, #e9ebf2 100%);
  }

  .tile {
    position: absolute; display: flex; align-items: center; justify-content: center;
    color: var(--white); border-radius: 20%;
    background: linear-gradient(180deg, var(--tile-top), var(--tile-bottom));
    border: 2px solid var(--white);
    box-shadow: 0 0 0 2px var(--tile-edge);
    line-height: 1;
  }
  .tile-small { width: 60px; height: 60px; font-size: 31px; }
  .tile-mid { width: 68px; height: 68px; font-size: 38px; }
  .tile-large { font-size: 62px; }

  .bracket { position: absolute; border: 2px solid var(--bracket); height: 10px; }
  .bracket-down { border-bottom: none; }
  .bracket-up { border-top: none; }

  .bubble {
    position: absolute; border-radius: 50%; border: 11px solid transparent;
    background:
      linear-gradient(var(--white), var(--white)) padding-box,
      linear-gradient(180deg, var(--ring-teal), var(--ring-blue)) border-box;
    display: flex; align-items: center; justify-content: center; text-align: center;
  }
  .bubble p { color: var(--text-dark); }
  .bubble em { font-style: normal; color: var(--brand-blue); }

  .footer { position: absolute; left: 0; top: 1148px; width: 849px; height: 52px; background: var(--footer-bg); }
  .footer-site { position: absolute; right: 30px; top: 15px; font-size: 17px; color: var(--white); }
</style>
</head>
<body>
<div class="poster">
  <header class="header">
    <div class="brand-mark"></div>
    <div class="brand-name">klangwerk-portal.de</div>
    <div class="brand-tagline">Veranstalungen einfach online pflegen</div>
  </header>
  <div class="rule" style="top:107px"></div>

  <div class="backdrop" role="img" aria-label="Hell überblendetes Foto eines Etikettendruckers mit bedruckten Lageretiketten"></div>

  <!-- Ebene Artikel -->
  <div class="tile tile-large" style="left:189px;top:199px;width:112px;height:115px">AR</div>
  <div class="bracket bracket-down" style="left:131px;top:328px;width:226px"></div>
  <div class="tile tile-small" style="left:141px;top:344px">EQ</div>
  <div class="tile tile-small" style="left:214px;top:344px">EQ</div>
  <div class="tile tile-small" style="left:287px;top:344px">EQ</div>

  <div class="bubble" style="left:539px;top:238px;width:216px;height:216px">
    <p style="font-size:23px;line-height:28px">Zu einem<br><em>Artikel</em> kann es<br>mehrere gleiche<br><em>Equipments</em><br>geben</p>
  </div>
  <div class="bubble" style="left:412px;top:138px;width:186px;height:186px">
    <p style="font-size:18.5px;line-height:24px">Der<br><em>Artikel</em> gibt die<br>Eigenschaften der<br><em>Equipments</em><br>vor.</p>
  </div>

  <div class="rule" style="top:475px"></div>

  <!-- Ebene Equipment, Set, Case -->
  <div class="bubble" style="left:73px;top:526px;width:234px;height:234px">
    <p style="font-size:19px;line-height:24px"><em>Equipments</em><br>können einzeln<br>gebucht oder in<br><em>Equipmentsets</em><br>und <em>Cases</em><br>zusammengefasst<br>werden.</p>
  </div>

  <div class="tile tile-mid" style="left:369px;top:610px">EQ</div>

  <div class="tile tile-small" style="left:487px;top:580px;width:53px;height:52px">EQ</div>
  <div class="tile tile-small" style="left:549px;top:580px;width:53px;height:52px">EQ</div>
  <div class="bracket bracket-up" style="left:479px;top:635px;width:129px"></div>
  <div class="tile tile-mid" style="left:510px;top:661px">ES</div>

  <div class="tile tile-small" style="left:658px;top:580px;width:53px;height:52px">EQ</div>
  <div class="tile tile-small" style="left:720px;top:580px;width:53px;height:52px">EQ</div>
  <div class="bracket bracket-up" style="left:650px;top:635px;width:129px"></div>
  <div class="tile tile-mid" style="left:680px;top:661px">CA</div>

  <div class="rule" style="top:808px"></div>

  <!-- Ebene Anlage -->
  <div class="tile tile-mid" style="left:135px;top:868px;width:69px;height:69px">EQ</div>
  <div class="tile tile-mid" style="left:216px;top:868px;width:69px;height:69px">ES</div>
  <div class="tile tile-mid" style="left:298px;top:868px;width:70px;height:69px">CA</div>
  <div class="bracket bracket-up" style="left:123px;top:945px;width:260px;height:12px"></div>
  <div class="tile tile-large" style="left:193px;top:974px;width:120px;height:120px">AN</div>

  <div class="bubble" style="left:467px;top:848px;width:268px;height:268px">
    <p style="font-size:22px;line-height:27px">In Anlagen<br>können einzelne<br><em>Equipments</em>, <em>Cases</em><br>und <em>Equipmentsets</em> in<br>beliebiger Anzahl und<br>Zusammenstellung<br>vorkommen.</p>
  </div>

  <footer class="footer">
    <div class="footer-site">klangwerk-portal.de</div>
  </footer>
</div>
</body>
</html>
```